Business Card Design

We recently had a new logo designed by Pixel Harbor. Now we want to create new business cards and letterhead that compliment our new logo.

We are audiologists in private practice specializing in hearing evaluations and fitting hearing aids. We want a clean and professional card.

We need business cards for each audiologist. The names and titles are:
Marnie Ostrova, AuD
Audiologist

Jen Tarbel, AuD
Audiologist

Corvina Plesk, AuD
Audiologist

We also need a business card with no provider. Just a generic one.

Finally, we need an appointment card. This is what the front desk uses to give to the patient with their next appointment date and time.

Target Market(s)

Our clients tend to be highly educated. They are older so the cards should be clean and easy to read. No squirrely font please.

Industry/Entity Type

Business

Contact Information for Business Card

20731 8th Ave NE, suite 417
Seattle, WA 98177
206-592-8074

Requirements
Must have
• Clean
Easy to read
Professional
Modern but approachable / warm
Should not have
• Other pictures besides the logo

```html
<!DOCTYPE html>
<html lang="en">
<head>
<meta charset="utf-8">
<title>Eastbrook Hearing Services – Business Card</title>
<link rel="stylesheet" href="https://fonts.googleapis.com/css2?family=Arimo:wght@400;700&display=swap">
<style>
  :root {
    --page-bg: #e9e8e6;
    --card-bg: #ffffff;
    --card-shade: #f1f1f2;
    --ink: #1d1d1f;
    --brand-navy: #2c4a66;
    --brand-teal: #4fae9c;
    --accent-soft: #a3a7bd;
  }
  html, body {
    margin: 0;
    padding: 0;
    width: 1200px;
    height: 848px;
    overflow: hidden;
    background: var(--page-bg);
    font-family: "Arimo", Arial, sans-serif;
  }
  .canvas {
    position: relative;
    width: 1200px;
    height: 848px;
    display: flex;
    align-items: center;
    justify-content: center;
  }
  .business-card {
    position: relative;
    width: 1050px;
    height: 600px;
    border-radius: 36px;
    background: linear-gradient(160deg, var(--card-bg) 55%, var(--card-shade) 100%);
    box-shadow: 0 10px 30px rgba(0,0,0,0.12);
    overflow: hidden;
    color: var(--ink);
  }
  .corner-accent {
    position: absolute;
    right: 0;
    bottom: 0;
    width: 360px;
    height: 360px;
  }
  .brand {
    position: absolute;
    left: 84px;
    top: 70px;
    display: flex;
    align-items: center;
    gap: 22px;
  }
  .brand-mark {
    width: 64px;
    height: 64px;
    border-radius: 50%;
    background: var(--brand-teal);
    flex: none;
  }
  .brand-block {
    display: flex;
    flex-direction: column;
  }
  .brand-name {
    font-weight: 700;
    font-size: 40px;
    letter-spacing: 3px;
    text-transform: uppercase;
    color: var(--brand-navy);
    line-height: 1.1;
  }
  .brand-tagline {
    margin-top: 8px;
    font-size: 18px;
    letter-spacing: 2px;
    color: var(--ink);
    font-style: italic;
  }
  .provider {
    position: absolute;
    left: 100px;
    top: 232px;
  }
  .provider-name {
    font-size: 42px;
    font-weight: 400;
    margin: 0;
    line-height: 1.1;
  }
  .provider-title {
    font-size: 22px;
    margin: 2px 0 0 8px;
  }
  .contact {
    position: absolute;
    left: 100px;
    top: 370px;
    font-size: 27px;
    line-height: 1.32;
    margin: 0;
    padding: 0;
    list-style: none;
  }
</style>
</head>
<body>
  <main class="canvas">
    <article class="business-card">
      <svg class="corner-accent" viewBox="0 0 360 360" aria-hidden="true">
        <circle cx="360" cy="360" r="300" fill="var(--accent-soft)" opacity="0.55"/>
      </svg>

      <header class="brand">
        <span class="brand-mark"></span>
        <div class="brand-block">
          <span class="brand-name">Eastbrook Hearing Services</span>
          <span class="brand-tagline">Clear care for every ear</span>
        </div>
      </header>

      <section class="provider">
        <h1 class="provider-name">Marnie Ostrova, AuD</h1>
        <p class="provider-title">Audiologist</p>
      </section>

      <ul class="contact">
        <li>P : 206-592-8074</li>
        <li>F : 206-592-8075</li>
        <li>www.eastbrookhearing.com</li>
        <li>20731 8th Ave NE, suite 417 Seattle, WA 98177</li>
      </ul>
    </article>
  </main>
</body>
</html>
```